Melissa Tarnow Personal Business Card

I like orange. It's would better if my card have an orange background
Address: 4720 Halberd Lane #318
San Jose
California
US
Tel: 4085172946

Industry/Entity Type

Business

```html
<!DOCTYPE html>
<html lang="en">
<head>
<meta charset="utf-8">
<title>Melissa Tarnow – Business Card</title>
<link rel="stylesheet" href="https://fonts.googleapis.com/css2?family=Exo+2:wght@400;500;700&display=swap">
<style>
  :root {
    --page-bg: #e4e4e6;
    --accent-bright: #f2711c;
    --accent-deep: #d9570f;
    --accent-mid: #e8641a;
    --ink: #1d1d1f;
    --card-white: #ffffff;
    --card-grey: #dcdcdc;
    --text-light: #ffffff;
  }
  * { margin: 0; padding: 0; box-sizing: border-box; }
  html, body {
    width: 1200px; height: 900px; overflow: hidden;
    background: var(--page-bg);
    font-family: "Exo 2", sans-serif;
  }
  .canvas {
    width: 1200px; height: 900px;
    display: flex; flex-direction: column; align-items: center; justify-content: center;
    gap: 48px;
  }
  .card {
    position: relative;
    width: 660px; height: 377px;
    box-shadow: 0 10px 28px rgba(0,0,0,.22);
    overflow: hidden;
  }
  /* Back side */
  .card-back {
    background: radial-gradient(ellipse at 55% 45%, var(--card-white) 0%, #f1f1f1 55%, var(--card-grey) 100%);
    display: flex; align-items: center; justify-content: center;
  }
  .brand { display: flex; align-items: center; gap: 16px; }
  .brand-dot {
    width: 78px; height: 78px; border-radius: 50%;
    background: var(--accent-bright);
    flex: none;
  }
  .brand-name {
    font-weight: 700; font-size: 40px; color: var(--ink);
    letter-spacing: .5px; white-space: nowrap;
  }
  /* Front side */
  .card-front { background: linear-gradient(90deg, #f4f4f4, var(--card-white) 70%, #ececec); }
  .front-shapes { position: absolute; inset: 0; }
  .contact {
    position: absolute; left: 40px; top: 36px;
    color: var(--text-light);
  }
  .person-name { font-size: 22px; font-weight: 500; letter-spacing: 1.5px; }
  .person-role { font-size: 15px; margin-top: 2px; letter-spacing: .5px; }
  .address { font-size: 17px; margin-top: 26px; line-height: 1.35; letter-spacing: .6px; }
  .channels { list-style: none; margin-top: 24px; }
  .channels li {
    display: flex; align-items: center; gap: 12px;
    font-size: 15px; letter-spacing: 1px; height: 27px;
  }
  .channels svg { width: 18px; height: 18px; flex: none; fill: none; stroke: var(--text-light); stroke-width: 1.6; }
  .front-brand {
    position: absolute; left: 432px; right: 8px; top: 118px;
    display: flex; flex-direction: column; align-items: center; gap: 12px;
  }
  .front-brand .brand-dot { width: 88px; height: 88px; }
  .front-brand .brand-name { font-size: 28px; }
</style>
</head>
<body>
<main class="canvas">
  <section class="card card-back" aria-label="Card back">
    <div class="brand">
      <span class="brand-dot"></span>
      <span class="brand-name">Melissa Tarnow</span>
    </div>
  </section>

  <section class="card card-front" aria-label="Card front">
    <svg class="front-shapes" viewBox="0 0 660 377" preserveAspectRatio="none" aria-hidden="true">
      <defs>
        <linearGradient id="accentFill" x1="0" y1="0" x2="1" y2="1">
          <stop offset="0" stop-color="#f2711c"/>
          <stop offset=".55" stop-color="#d9570f"/>
          <stop offset="1" stop-color="#ee6a18"/>
        </linearGradient>
      </defs>
      <path d="M0 0 H430 Q370 190 452 377 H0 Z" fill="url(#accentFill)"/>
      <path d="M430 0 Q370 190 452 377 H466 Q384 190 444 0 Z" fill="#1d1d1f"/>
    </svg>

    <div class="contact">
      <p class="person-name">DANIEL WHITFORD</p>
      <p class="person-role">Managing Director</p>
      <p class="address">4720 Halberd Lane #318<br>San Jose, CA</p>
      <ul class="channels">
        <li><svg viewBox="0 0 20 20"><path d="M5 2 L8 6 L6.5 8 Q8 12 12 13.5 L14 12 L18 15 L16 18 Q6 17 2 5 Z"/></svg>408 517 2946</li>
        <li><svg viewBox="0 0 20 20"><rect x="6" y="2" width="8" height="16" rx="1.5"/><line x1="9" y1="15.5" x2="11" y2="15.5"/></svg>408 517 2946</li>
        <li><svg viewBox="0 0 20 20"><rect x="3" y="7" width="14" height="10" rx="1"/><rect x="6" y="2" width="8" height="5"/><line x1="6" y1="11" x2="14" y2="11"/></svg>408 517 2946</li>
        <li><svg viewBox="0 0 20 20"><rect x="2" y="4" width="16" height="12"/><path d="M2 4 L10 11 L18 4"/></svg>hello@tarnowmail.com</li>
        <li><svg viewBox="0 0 20 20"><circle cx="10" cy="10" r="8"/><ellipse cx="10" cy="10" rx="3.5" ry="8"/><line x1="2" y1="10" x2="18" y2="10"/></svg>www.melissatarnow.com</li>
      </ul>
    </div>

    <div class="front-brand">
      <span class="brand-dot"></span>
      <span class="brand-name">Melissa Tarnow</span>
    </div>
  </section>
</main>
</body>
</html>
```